Corporate Stationary for Beverage Alcohol Company
Brook Harbor Global Ltd. Co.
Corporate Stationary for Beverage Alcohol Company - Beverages
Creative Brief
Corporate
Dean Walter Prosser
President
512 Fenwood Drive Richmond, KY 40475
dean.prosser@brook-harbor.com
www.brook-harbor.com
The stationary shall be cutting edge and will utilize the logo art work. I would like an abstract border included on the side(s) of the letterhead, envelope and the business card.
Company Name Logo Abstract border

```html
<!DOCTYPE html>
<html lang="en">
<head>
<meta charset="utf-8">
<title>Brook Harbor Global – Business Card</title>
<link href="https://fonts.googleapis.com/css2?family=Cinzel:wght@400;600&family=Libre+Baskerville&display=swap" rel="stylesheet">
<style>
  :root {
    --bg: #d9d9d9;
    --gold-light: #f3d27e;
    --gold: #d9a53f;
    --gold-deep: #b07a1c;
    --ink: #1a1a1a;
    --text: #444;
    --white: #ffffff;
    --rule: #c9c9c9;
  }
  * { margin: 0; padding: 0; box-sizing: border-box; }
  html, body { width: 1200px; height: 871px; overflow: hidden; background: var(--bg); }
  .canvas {
    width: 1200px; height: 871px;
    display: flex; flex-direction: column; align-items: center; justify-content: center; gap: 30px;
  }
  .card {
    width: 700px; height: 400px; position: relative; overflow: hidden;
    box-shadow: 0 6px 18px rgba(0,0,0,.18);
  }
  /* Front */
  .card-front .pattern {
    position: absolute; inset: 0;
    background: radial-gradient(ellipse at 45% 40%, var(--gold-light), var(--gold) 55%, var(--gold-deep));
  }
  .card-front .brand {
    position: absolute; left: 0; right: 0; top: 170px;
    display: flex; align-items: center; justify-content: center; gap: 14px;
  }
  .brand-mark { width: 14px; height: 14px; border-radius: 50%; background: currentColor; }
  .brand-name {
    font-family: "Cinzel", serif; font-weight: 600; letter-spacing: 1px;
  }
  .card-front .brand { color: var(--white); }
  .card-front .brand-name { font-size: 34px; }
  /* Back */
  .card-back { background: var(--white); }
  .card-back svg.swoosh { position: absolute; inset: 0; }
  .card-back .brand {
    position: absolute; left: 40px; top: 210px; color: var(--ink);
    display: flex; align-items: center; gap: 10px;
  }
  .card-back .brand-name { font-size: 22px; }
  .card-back .brand-mark { width: 10px; height: 10px; }
  .holder {
    position: absolute; right: 40px; top: 255px; text-align: right;
    font-family: "Cinzel", serif;
  }
  .holder-name { font-size: 20px; color: var(--ink); letter-spacing: .5px; }
  .holder-title { font-size: 14px; color: var(--gold); margin-top: 2px; }
  .contact {
    position: absolute; left: 40px; top: 275px; list-style: none;
    font-family: "Libre Baskerville", serif; font-size: 13px; color: var(--text); line-height: 24px;
  }
  .contact li { display: flex; align-items: center; gap: 8px; }
  .contact svg { width: 11px; height: 11px; fill: var(--gold); flex: none; }
  .contact .address { padding-left: 19px; }
</style>
</head>
<body>
<main class="canvas">
  <section class="card card-front">
    <div class="pattern" role="img" aria-label="Gold background with a fine repeating decorative pattern"></div>
    <div class="brand">
      <span class="brand-mark"></span>
      <span class="brand-name">BROOK HARBOR GLOBAL</span>
    </div>
  </section>

  <section class="card card-back">
    <svg class="swoosh" viewBox="0 0 700 400" aria-hidden="true">
      <defs>
        <linearGradient id="goldBand" x1="0" y1="0" x2="1" y2="1">
          <stop offset="0" stop-color="#f3d27e"/>
          <stop offset=".55" stop-color="#d9a53f"/>
          <stop offset="1" stop-color="#b07a1c"/>
        </linearGradient>
      </defs>
      <path d="M0 0H700V28C480 38 250 80 0 160Z" fill="url(#goldBand)"/>
      <path d="M0 172C250 92 480 50 700 42V52C480 62 250 104 0 186Z" fill="#1a1a1a"/>
      <path d="M0 198C250 118 480 76 700 68" fill="none" stroke="#c9c9c9" stroke-width="1.5"/>
    </svg>
    <div class="brand">
      <span class="brand-mark"></span>
      <span class="brand-name">BROOK HARBOR GLOBAL</span>
    </div>
    <div class="holder">
      <div class="holder-name">Dean Walter Prosser</div>
      <div class="holder-title">PRESIDENT</div>
    </div>
    <ul class="contact">
      <li class="address">512 Fenwood Drive, Richmond, KY 40475</li>
      <li><svg viewBox="0 0 10 10"><path d="M2 0h2l1 3-1.5 1a6 6 0 0 0 2.5 2.5L7 5l3 1v2a2 2 0 0 1-2 2A8 8 0 0 1 0 2a2 2 0 0 1 2-2z"/></svg>(859)-555-0142</li>
      <li><svg viewBox="0 0 10 10"><path d="M0 2h10v6H0z M0 2l5 3 5-3" stroke="#fff" stroke-width=".8"/></svg>dean.prosser@brook-harbor.com</li>
      <li><svg viewBox="0 0 10 10"><circle cx="5" cy="5" r="5"/></svg>www.brook-harbor.com</li>
    </ul>
  </section>
</main>
</body>
</html>
```